Spa Business Card Design Project

Hello! We are a boutique spa for men and women that is rebranding. I would like a memorable new business card that showcases our beautiful new logo and our unique business. I would like it to be classic/timeless and eclectic/artistic at the  same time.
I am a fan of negative space as you can tell from the logo. I am also open to any creative ideas.
Multi sided design. Two sided design is acceptable as an option, too. "Flaps/folds/whatever the design term is" are optional- whether full vertical or horizontal, half flap, full flap etc
On either side next to the golden snail I would potentially like to see "slow down. Enjoy Life."  Possibly on one statment on top of each other, crowned with the snail. Or the statment following the snail on one line... I am open for a creative suprise, too.
The back I would like room for the standard Information
"3817 Birch Lane
Halden, New York 12485
(518) 462 3085
info@thecorvella spa.com
The snail is to be done in gold ink.
Can I also Have an option for cards that are individualized for staff members, too?

Updates
Project Deadline Extended
Reason: I apologize for the deadline extension. My day was more involved than anticipated in other matters. Hope to have this closed by next Tuesday.
Thank you

Target Market(s)
Men and women with expendable income between the ages of 30-55
Industry/Entity Type
Boutique
Requirements
Must have
- only black and gold ink.

Nice to have
- One of a kind.
Showcase the snail :-)
make you smile :-)
Fun, but professional.
Should not have
- Lots of color.
Too feminine.
Too busy.

```html
<!DOCTYPE html>
<html lang="en">
<head>
<meta charset="utf-8">
<title>The Corvella Spa – Folded Business Card</title>
<link rel="stylesheet" href="https://fonts.googleapis.com/css2?family=Cinzel:wght@400;600&family=Questrial&display=swap">
<style>
  :root {
    --backdrop: #2b2b2d;
    --card: #1c1d21;
    --fold: #4a4b50;
    --ink-black: #0d0e10;
    --ink-deep: #34353a;
    --gold: #c9a45c;
    --white: #f2f2f2;
    --muted: #55565b;
  }
  * { margin: 0; padding: 0; box-sizing: border-box; }
  html, body { width: 1200px; height: 900px; overflow: hidden; background: var(--backdrop); }
  .canvas { position: relative; width: 1200px; height: 900px; }

  .card {
    position: absolute; top: 140px; width: 510px; height: 618px;
    background: var(--card);
    box-shadow: 0 4px 14px rgba(0,0,0,0.45);
  }
  .card--outside { left: 77px; }
  .card--inside { left: 615px; }
  .card__fold {
    position: absolute; left: 0; right: 0; top: 310px; height: 1px; background: var(--fold);
  }
  .panel { position: absolute; left: 0; right: 0; text-align: center; }
  .panel--top { top: 0; height: 310px; }
  .panel--bottom { top: 311px; height: 307px; }

  /* Outside: address printed upside down on the top flap */
  .address {
    position: absolute; left: 0; right: 0; top: 140px;
    transform: rotate(180deg);
    font-family: "Questrial", sans-serif; font-size: 13.5px; line-height: 16px;
    color: var(--gold); text-align: center;
  }

  .brand-mark {
    position: absolute; left: 0; right: 0; top: 70px;
    font-family: "Cinzel", serif; font-weight: 400; font-size: 58px; line-height: 60px;
    color: var(--ink-deep); letter-spacing: 1px;
  }
  .brand-mark__line { display: block; }
  .brand-mark__tagline {
    position: absolute; left: 0; right: 0; top: 220px;
    font-family: "Questrial", sans-serif; font-size: 16px; color: var(--muted);
  }

  /* Inside: slogan */
  .slogan {
    position: absolute; left: 0; right: 0; top: 98px;
    font-family: "Cinzel", serif; font-weight: 600; color: var(--ink-black);
    font-size: 37px; line-height: 1; letter-spacing: 1px;
  }
  .slogan__line { display: block; }
  .slogan__dot {
    display: block; width: 14px; height: 14px; margin: 15px auto 17px;
    border-radius: 50%; background: var(--gold);
  }

  .logo-name {
    position: absolute; left: 0; right: 0; top: 36px;
    font-family: "Cinzel", serif; font-weight: 400; font-size: 32px; line-height: 34px;
    color: var(--white);
  }
  .logo-name__line { display: block; }
  .logo-tagline {
    position: absolute; left: 0; right: 0; top: 131px;
    font-family: "Questrial", sans-serif; font-size: 11px; color: var(--white);
  }
  .staff-name {
    position: absolute; left: 0; right: 0; top: 179px;
    font-family: "Cinzel", serif; font-weight: 600; font-size: 23px; color: var(--gold);
    letter-spacing: 0.5px;
  }
  .staff-role {
    position: absolute; left: 0; right: 0; top: 208px;
    font-family: "Questrial", sans-serif; font-size: 17px; color: var(--white);
  }
  .contact {
    position: absolute; left: 0; right: 0; top: 243px;
    font-family: "Questrial", sans-serif; font-size: 13.5px; line-height: 18px; color: var(--white);
  }
</style>
</head>
<body>
<main class="canvas">
  <section class="card card--outside" aria-label="Card outside">
    <div class="panel panel--top">
      <p class="address">3817 Birch Lane<br>Halden, New York 12485</p>
    </div>
    <div class="card__fold"></div>
    <div class="panel panel--bottom">
      <p class="brand-mark">
        <span class="brand-mark__line">The Corvella</span>
        <span class="brand-mark__line">Spa</span>
      </p>
      <p class="brand-mark__tagline">a boutique spa for Men &amp; Women</p>
    </div>
  </section>

  <section class="card card--inside" aria-label="Card inside">
    <div class="panel panel--top">
      <p class="slogan">
        <span class="slogan__line">Slow Down</span>
        <span class="slogan__dot" aria-hidden="true"></span>
        <span class="slogan__line">Enjoy Life</span>
      </p>
    </div>
    <div class="card__fold"></div>
    <div class="panel panel--bottom">
      <p class="logo-name">
        <span class="logo-name__line">The Corvella</span>
        <span class="logo-name__line">Spa</span>
      </p>
      <p class="logo-tagline">a boutique spa for Men &amp; Women</p>
      <p class="staff-name">Daniel Harrow</p>
      <p class="staff-role">founder &amp; owner</p>
      <p class="contact">(518) 462 3085<br>info@thecorvella spa.com</p>
    </div>
  </section>
</main>
</body>
</html>
```